Roster'd book cover required for a novel! Print and Ebook- Please see attached image

MY PEN NAME IS MARA HOLT.
Apologies to everyone that I have updated my brief.
On the front cover I would like Roster'd written in quite bold font (modern) and an image of an out line (silhouette) of a woman (Just like would be on a toilet door for women) holding hands with the silhouette of a domestic plane. I imagine the silhouettes to be black or dark grey and the font to be red with a white background.
Updates

Project Deadline Extended
Reason: I have struggled with my brief to know what to ask designers for but I have come up with a better idea and would love to extend to see if my brief is much clearer xx

Target Market(s)

Women

Industry/Entity Type

Book Publisher

Font styles to use
Serif
Sans Serif

Colors

Designer to choose colors to be used in the design.

Requirements
Must have
• Front, back and spine for a paperback and also a design for an ebook.
• Blurb: FIFO, the other four lettered F word.
• Roster’d tells the story of three women who swing from time with their fly-in fly-out lovers to time alone.
• Tessa swings from one week with Gary, to two weeks without. She is strong, messy and full of heart. Can she survive the chaos and the separation?
• Tessa’s younger sister, Nina, swings from one week with Rob, to three weeks alone. She craves attention and goes looking for it in likely places. Nina is not sure that one week in a month is enough for a marriage to survive.
• Nina doesn’t know that Rob also spends one week with Dora, who then spends three weeks by herself. Dora has lost the blueprint that was going to lead her somewhere fabulous. She lost her mother and her bearings. With a new job researching women in violent relationships, she is trying to work it all out.
• This is a story of dirt, coastal froth, loneliness, airports, fish, rosters, phone calls, mines, distance, time, country, independence, stars, laughter, sex and imperfect days.
• A white rectangle for an ISBN number on the back cover.
Nice to have
• As above

```html
<!DOCTYPE html>
<html lang="en">
<head>
<meta charset="utf-8">
<title>Roster'd — Mara Holt — Cover Wrap</title>
<link rel="stylesheet" href="https://fonts.googleapis.com/css2?family=Montserrat:wght@400;500;800&family=Open+Sans:ital,wght@1,400&family=Roboto+Condensed:wght@300;400;700&display=swap">
<style>
  :root {
    --stage: #ececec;
    --ocean-deep: #0d4f74;
    --ocean-mid: #1b83b0;
    --ocean-light: #3fb3cf;
    --surf: #d9eef2;
    --sand: #e6eaea;
    --palm: #2f6b3a;
    --title-red: #c8202b;
    --silhouette: #2b2f33;
    --peach: #f2c48d;
    --white: #ffffff;
    --ink: #1d2f3a;
    --panel: rgba(255, 255, 255, 0.82);
    --quote-mark: rgba(220, 225, 228, 0.45);
  }
  * { box-sizing: border-box; margin: 0; padding: 0; }
  html, body {
    width: 1200px; height: 800px; overflow: hidden;
    background: var(--stage);
  }
  .wrap {
    position: absolute; left: 220px; top: 130px;
    width: 760px; height: 540px;
    display: flex;
    box-shadow: 0 14px 30px rgba(0,0,0,0.18);
  }
  .cover, .spine { position: relative; height: 540px; overflow: hidden; }
  .cover { width: 360px; }
  .spine { width: 40px; }

  .photo { position: absolute; inset: 0; }
  .photo--front {
    background:
      linear-gradient(125deg, transparent 62%, var(--surf) 68%, var(--sand) 73%, var(--sand) 82%, var(--palm) 90%, #3d7d46 100%),
      linear-gradient(160deg, var(--ocean-deep) 0%, var(--ocean-mid) 45%, var(--ocean-light) 80%);
  }
  .photo--back {
    background:
      linear-gradient(55deg, transparent 0%, transparent 100%),
      linear-gradient(200deg, var(--ocean-light) 0%, var(--ocean-mid) 40%, var(--ocean-deep) 100%);
  }
  .photo--spine {
    background: linear-gradient(180deg, var(--ocean-deep), var(--ocean-mid) 60%, var(--ocean-deep));
  }

  /* Front */
  .quote-mark {
    position: absolute; font-family: Georgia, serif; font-size: 80px;
    line-height: 1; color: var(--quote-mark); font-weight: 700;
  }
  .quote-mark--open { top: 18px; left: 22px; }
  .quote-mark--close { top: 58px; right: 22px; }
  .front__quote {
    position: absolute; top: 42px; left: 64px; right: 64px;
    font-family: "Open Sans", sans-serif; font-style: italic;
    font-size: 11.5px; line-height: 1.35; letter-spacing: 0.3px;
    color: var(--white); text-align: center;
  }
  .front__label {
    position: absolute; top: 128px; left: 0; right: 0;
    font-family: "Montserrat", sans-serif; font-size: 12px;
    letter-spacing: 2px; color: var(--white); text-align: center;
  }
  .title-box {
    position: absolute; top: 156px; left: 40px; width: 280px; height: 124px;
    background: var(--white);
    text-align: center;
    padding-top: 18px;
  }
  .title {
    font-family: "Montserrat", sans-serif; font-weight: 800;
    font-size: 46px; letter-spacing: 1px; color: var(--title-red);
    line-height: 1.1; white-space: nowrap;
  }
  .subtitle {
    margin-top: 10px;
    font-family: "Roboto Condensed", sans-serif; font-weight: 400;
    font-size: 17px; color: var(--ink); letter-spacing: 0.4px;
  }
  .silhouette {
    position: absolute; top: 306px; left: 105px; width: 150px; height: 150px;
    border-radius: 50%;
    background: var(--silhouette); opacity: 0.85;
  }
  .front__author {
    position: absolute; bottom: 26px; left: 0; right: 0;
    font-family: "Montserrat", sans-serif; font-weight: 500;
    font-size: 20px; letter-spacing: 11px; color: var(--ink);
    text-align: center;
  }

  /* Spine */
  .spine__title {
    position: absolute; top: 22px; left: 50%; transform: translateX(-50%);
    writing-mode: vertical-rl;
    font-family: "Montserrat", sans-serif; font-weight: 800;
    font-size: 16px; letter-spacing: 2px; color: var(--white);
  }
  .spine__author {
    position: absolute; bottom: 24px; left: 50%; transform: translateX(-50%);
    writing-mode: vertical-rl;
    font-family: "Montserrat", sans-serif; font-size: 11px;
    letter-spacing: 5px; color: var(--white);
  }

  /* Back */
  .blurb {
    position: absolute; top: 34px; left: 34px; width: 292px; height: 330px;
    background: var(--panel); padding: 16px 16px 0;
    font-family: "Roboto Condensed", sans-serif; color: var(--ink);
  }
  .blurb__lead {
    font-weight: 700; font-size: 11.5px; line-height: 1.3;
    text-align: center; padding: 0 8px;
  }
  .blurb__rule { width: 40px; height: 2px; background: var(--title-red); margin: 9px auto 11px; }
  .blurb__para { font-size: 9.6px; line-height: 1.32; margin-bottom: 8px; }
  .bio {
    position: absolute; top: 378px; left: 34px; width: 292px;
    font-family: "Roboto Condensed", sans-serif; font-size: 9.6px;
    line-height: 1.4; color: var(--white);
  }
  .bio__name { color: var(--peach); font-weight: 700; }
  .isbn-box {
    position: absolute; bottom: 28px; left: 34px;
    width: 120px; height: 62px; background: var(--white);
  }
  .price {
    position: absolute; bottom: 30px; left: 164px;
    font-family: "Roboto Condensed", sans-serif; font-size: 8px;
    line-height: 1.4; color: var(--white);
  }
  .publisher {
    position: absolute; bottom: 30px; right: 34px;
    display: flex; align-items: center; gap: 6px;
    font-family: "Roboto Condensed", sans-serif; font-size: 10px;
    letter-spacing: 1px; color: var(--white);
  }
  .publisher__square { width: 12px; height: 12px; background: var(--white); }
</style>
</head>
<body>
  <main class="wrap">
    <section class="cover cover--back">
      <div class="photo photo--back" role="img" aria-label="Aerial photograph of turquoise ocean water"></div>
      <div class="blurb">
        <p class="blurb__lead">Roster’d tells the story of three women who swing from time with their fly-in fly-out lovers to time alone.</p>
        <div class="blurb__rule"></div>
        <p class="blurb__para">Tessa swings from one week with Gary, to two weeks without. She is strong, messy and full of heart. Can she survive the chaos and the separation?</p>
        <p class="blurb__para">Tessa’s younger sister, Nina, swings from one week with Rob, to three weeks alone. She craves attention and goes looking for it in likely places. Nina is not sure that one week in a month is enough for a marriage to survive.</p>
        <p class="blurb__para">Nina doesn’t know that Rob also spends one week with Dora, who then spends three weeks by herself. Dora has lost the blueprint that was going to lead her somewhere fabulous. She lost her mother and her bearings. With a new job researching women in violent relationships, she is trying to work it all out.</p>
        <p class="blurb__para">This is a story of dirt, coastal froth, loneliness, airports, fish, rosters, phone calls, mines, distance, time, country, independence, stars, laughter, sex and imperfect days.</p>
      </div>
      <p class="bio"><span class="bio__name">MARA HOLT</span> (short description about author) lorem ipsum dolor sit amet, consectetur adipiscing elit, sed do eiusmod tempor incididunt ut labore et dolore magna aliqua. Ut enim ad minim veniam, quis nostrud exercitation ullamco laboris nisi ut aliquip ex ea commodo consequat.</p>
      <div class="isbn-box" aria-label="Space for ISBN"></div>
      <p class="price">AU$ 123.45<br>NZ$ 123.45</p>
      <div class="publisher"><span class="publisher__square"></span><span>COASTLINE PRESS</span></div>
    </section>

    <section class="spine">
      <div class="photo photo--spine" role="img" aria-label="Deep blue ocean photograph continuing across the spine"></div>
      <span class="spine__title">Roster’d</span>
      <span class="spine__author">MARA HOLT</span>
    </section>

    <section class="cover cover--front">
      <div class="photo photo--front" role="img" aria-label="Aerial photograph of turquoise ocean meeting a white sand beach and palm trees"></div>
      <span class="quote-mark quote-mark--open">“</span>
      <span class="quote-mark quote-mark--close">”</span>
      <p class="front__quote">A story of three women who swing from time with their fly-in fly-out lovers to time alone</p>
      <p class="front__label">A NOVEL</p>
      <div class="title-box">
        <h1 class="title">Roster’d</h1>
        <p class="subtitle">the other four lettered F word</p>
      </div>
      <div class="silhouette" role="img" aria-label="Dark silhouette of a woman holding hands with a small domestic plane"></div>
      <p class="front__author">MARA HOLT</p>
    </section>
  </main>
</body>
</html>
```